Wordpress Web Design & Coding for velnoragroup.ca

We need a website for a new investment company that is visually grabbing and vibrant. We would like to see a web page that displays trust, growth and confidence. Needs to be responsive and mobile friendly for all browsers and coded for both Android & IOS.

Open to the number of pages and menu items. I selected 4 but if you feel the layout would work better with less I am open to this. Need to sell the people (management team/related businesses) and then show where the invested money will be going (upcoming projects).

Company Info:

Velnora is an investment company put together by a group of seasoned business professionals who have come together to combine decades of success in the real estate development, management, financing and medical services. The company will be a full service company offering turn key solutions for medical professionals.

Vel-Nora will focus on providing a full range of services via a group of distinct companies to deliver newly emerging needs of the medical community. The end goal will be to create complete solutions for individuals in the medical community. Our group has experience and success with the conceptualization, construction and financing of medical and dental clinic spaces. Vel-Nora Group will be established to accommodate all areas of the development and creation of clinics for medical professionals from building construction to equipment financing and administrations.

You can mention these companies and take photos from their websites. You can also use stock photos.

Our construction partner:
https://382bld.com/projects/

Our equipment leasing partner:
https://www.pordiva.com/

Our Management Team and medical partners

Gil Parkes
https://www.mysoundpoise.ca/

Milos Vendraker
https://www.qrtdentalservices.com/about-us

PROPOSED PROJECTS (see attachment for details)
Hollowmere Business Park
Cresfield Business Park
Mt. Corwin Ridge Professional

Investors

Investment

Sans Serif

Must have
• Wordpress – must be both desktop and mobile friendly with fast page load speed
Ability to edit after ourselves in Wordpress
Attractive home page with logo etc.
Logo colours are: for the blue the pantone color is #0355a3
and for the green is #8cc63f

Sections, about us, what we do/services we provide, contact us

```html
<!DOCTYPE html>
<html lang="en">
<head>
<meta charset="utf-8">
<title>Vel-Nora Group</title>
<link rel="stylesheet" href="https://fonts.googleapis.com/css2?family=Montserrat:wght@400;500;600;700;800&family=Oswald:wght@500&display=swap">
<style>
:root{
  --blue:#0355a3;
  --green:#8cc63f;
  --ink:#1d1d1d;
  --text:#333;
  --muted:#555;
  --soft:#f4f6f8;
  --foot:#232425;
}
*{box-sizing:border-box;margin:0;padding:0}
html,body{width:1200px;height:3586px;overflow:hidden}
body{position:relative;font-family:'Montserrat',sans-serif;color:var(--text);background:#fff}
.abs{position:absolute}
.btn{position:absolute;display:flex;align-items:center;justify-content:center;gap:6px;background:var(--green);color:#fff;font-size:14px;font-weight:500;border-radius:3px;letter-spacing:.3px}
.two{font-weight:700;font-size:40px;letter-spacing:.5px}
.two .b{color:var(--blue)}.two .g{color:var(--green)}
.center{left:0;width:1200px;text-align:center}

/* header */
.brand{left:140px;top:52px;font-size:28px;font-weight:700;color:var(--blue);display:flex;align-items:center;gap:10px}
.brand i{width:16px;height:16px;background:var(--green);display:block}
.topc{top:19px;display:flex;align-items:center;gap:10px;font-size:15px;font-weight:500;color:var(--ink)}
.topc span.ic{width:26px;height:26px;background:var(--green);border-radius:3px;display:flex;align-items:center;justify-content:center}
.nav{top:72px;font-size:14px;color:#444;font-weight:500}
.nav.on{color:var(--blue);font-weight:700}
.hero-photo{left:0;top:0;width:1200px;height:466px}
.hero-text{left:143px;top:176px;font-family:'Oswald',sans-serif;font-weight:500;font-size:22px;line-height:36px;color:var(--ink)}

/* about */
.about-photo{left:0;top:465px;width:470px;height:684px}
.about-h{left:465px;top:585px;font-size:25px;color:var(--blue);font-weight:500}
.about-t{left:465px;top:620px}
.lead{left:465px;top:682px;width:600px;font-size:15.5px;line-height:30px;font-weight:500;color:var(--ink)}
.body-s{left:465px;width:592px;font-size:11.5px;line-height:23px;color:var(--muted);text-align:justify}

/* solutions */
.sol-img{top:1302px;width:428px;height:246px}
.band{left:0;top:1570px;width:1200px;height:296px;background:linear-gradient(180deg,#2a66b0,#3f7cc2 60%,#2e68b2)}
.sol-card{top:1570px;width:438px;height:133px;background:#fff;text-align:center;padding:0 40px;box-shadow:0 6px 18px rgba(0,0,0,.08)}
.sol-card h3{font-size:18px;font-weight:500;color:var(--ink);margin-top:18px;letter-spacing:.3px}
.sol-card p{font-size:11px;line-height:23px;color:#333;margin-top:8px}

/* projects */
.proj-img{top:2015px;width:292px;height:338px}
.proj-card{top:2282px;width:250px;height:113px;background:#fff;border-bottom:3px solid var(--green);padding:14px 12px;box-shadow:0 4px 14px rgba(0,0,0,.08)}
.proj-card h4{font-size:15.5px;font-weight:700;color:var(--ink);white-space:nowrap}
.proj-card p{font-size:10px;line-height:20px;color:#333;margin-top:8px}
.arrow{top:2166px;width:34px;height:34px;border-radius:50%;display:flex;align-items:center;justify-content:center}

/* team */
.soft{left:0;top:2477px;width:1200px;height:481px;background:var(--soft)}
.tab{top:2546px;height:41px;border:2px solid var(--blue);border-radius:3px;display:flex;align-items:center;justify-content:center;font-size:14px;font-weight:500}
.team{top:2630px;width:438px;height:252px;background:#fff;box-shadow:0 4px 14px rgba(0,0,0,.06)}
.team .ph{position:absolute;left:4px;top:4px;width:217px;height:244px}
.team .info{position:absolute;left:238px;top:30px;width:190px}
.team h5{font-size:15.5px;font-weight:700;color:var(--blue)}
.team .co{font-size:19px;color:#777;margin:10px 0 14px;font-weight:400}
.team p{font-size:10px;line-height:20px;color:#333}

/* newsletter */
.news-art{left:148px;top:3032px;width:230px;height:226px;background:linear-gradient(160deg,#eaf4dc,#d3e8b6 60%,#c4d9ec);border-radius:4px}
.news-h{left:415px;top:3045px}
.news-q{left:420px;top:3112px;font-size:15.5px;color:var(--ink);font-weight:500}
.news-s{left:420px;top:3140px;font-size:15px;color:var(--green)}
.field{left:420px;top:3191px;width:413px;height:50px;border:1px solid #d4d4d4;border-radius:3px;font-size:10px;color:#777;padding:0 20px;display:flex;align-items:center}

/* footer */
.foot{left:0;top:3330px;width:1200px;height:256px;background:var(--foot);color:#fff}
.fnav{top:3379px;font-size:13.5px;font-weight:500;color:#fff}
.sep{top:3380px;width:1px;height:14px;background:#666}
.fline{left:0;width:1200px;height:1px;background:#3a3a3a}
.fi{top:3451px;display:flex;gap:12px;align-items:flex-start;color:#fff}
.fi .c{width:34px;height:34px;border:2px solid #fff;border-radius:50%;display:flex;align-items:center;justify-content:center;flex:none}
.fi b{font-size:13.5px;font-weight:600;display:block}
.fi small{font-size:11px;line-height:17px;display:block;margin-top:2px}
.vsep{top:3450px;width:0;height:50px;border-left:1px dashed #666}
.copy{left:142px;top:3555px;font-size:11px;color:#ddd}
.soc{top:3552px;width:24px;height:24px;border:1.5px solid #fff;border-radius:50%}
</style>
</head>
<body>

<!-- header -->
<svg class="abs hero-photo" viewBox="0 0 1200 466" role="img" aria-label="Photo of glass skyscrapers against a blue sky"><defs><linearGradient id="sky" x1="0" y1="0" x2="0" y2="1"><stop offset="0" stop-color="#dbe9f6"/><stop offset=".5" stop-color="#5d98cf"/><stop offset="1" stop-color="#1a4f8c"/></linearGradient></defs><polygon points="630,0 815,0 1176,466 470,466" fill="url(#sky)"/></svg>
<div class="abs brand"><i></i>VEL-NORA GROUP</div>
<div class="abs topc" style="left:645px"><span class="ic"><svg width="14" height="14" viewBox="0 0 24 24" fill="#fff"><path d="M6.6 10.8a15 15 0 0 0 6.6 6.6l2.2-2.2a1 1 0 0 1 1-.25 11.4 11.4 0 0 0 3.6.57 1 1 0 0 1 1 1V20a1 1 0 0 1-1 1A17 17 0 0 1 3 4a1 1 0 0 1 1-1h3.5a1 1 0 0 1 1 1c0 1.25.2 2.45.57 3.57a1 1 0 0 1-.25 1z"/></svg></span>+1 555 014 2288</div>
<div class="abs topc" style="left:818px"><span class="ic"><svg width="14" height="12" viewBox="0 0 24 18" fill="none" stroke="#fff" stroke-width="2"><rect x="1" y="1" width="22" height="16"/><path d="M1 1l11 9 11-9"/></svg></span>info@velnoragroup.ca</div>
<div class="abs nav on" style="left:583px">HOME</div>
<div class="abs nav" style="left:681px">ABOUT US</div>
<div class="abs nav" style="left:809px">WHAT WE DO</div>
<div class="abs nav" style="left:962px">CONTACT US</div>
<div class="abs hero-text">Vel-Nora Is An Investment Company<br>With Focus on Providing A Full Range<br>of Services, For The Newly Emerging<br>Needs of The Medical Community</div>
<div class="btn" style="left:142px;top:334px;width:172px;height:38px">CALL US TODAY →</div>

<!-- about -->
<svg class="abs about-photo" viewBox="0 0 470 684" role="img" aria-label="Photo of nurses wheeling a hospital bed down a bright corridor"><defs><linearGradient id="hall" x1="0" y1="0" x2="1" y2="1"><stop offset="0" stop-color="#bfe3ee"/><stop offset=".5" stop-color="#5fb3d3"/><stop offset="1" stop-color="#1f6f9c"/></linearGradient></defs><polygon points="0,0 460,0 120,684 0,684" fill="url(#hall)"/></svg>
<div class="abs about-h">ABOUT</div>
<div class="abs about-t two"><span class="b">VEL-NORA</span> <span class="g">GROUP</span></div>
<div class="abs lead">Vel-Nora will focus on providing a full range of services via a group of distinct companies to deliver newly emerging needs of the medical community.</div>
<div class="abs body-s" style="top:783px">The end goal will be to create complete solutions for individuals in the medical community. Our group has experience and success with the conceptualization, construction and financing of medical and dental clinic spaces. Vel-Nora Group will be established to accommodate all areas of the development and creation of clinics for medical professionals from building construction to equipment financing and administrations.</div>
<div class="abs body-s" style="top:909px">The company's operation will be managed in Sherwood Park, Alberta facilitating transactions across western Canada. It will be structured in a tax efficient manner for our investors. The income will be treated as active income to allow for an efficient growth of earnings.</div>
<div class="btn" style="left:463px;top:1008px;width:142px;height:38px">READ MORE →</div>

<!-- solutions -->
<div class="abs center two" style="top:1212px"><span class="b">VEL-NORA</span> <span class="g">GROUP</span></div>
<div class="abs band" role="img" aria-label="Blue-tinted photo of a business meeting"></div>
<div class="abs sol-img" style="left:146px;background:linear-gradient(135deg,#1b3f78,#4a7fc0 55%,#c9d6e6)" role="img" aria-label="Photo of a hand touching a hexagon leasing interface"></div>
<div class="abs sol-img" style="left:626px;background:radial-gradient(circle at 50% 45%,#6c8fbf,#1b2f5a 70%)" role="img" aria-label="Photo of hands holding a glowing security shield"></div>
<div class="abs sol-card" style="left:141px"><h3>LEASING OPERATIONS</h3><p>Vel-Nora Group leasing division will secure an investment portfolio comprised of equipment leases and other small business financing solutions across Western Canada...[+]</p></div>
<div class="abs sol-card" style="left:621px"><h3>SECURITY MEASURES</h3><p>Vel-Nora Group leasing divison will implement a number of security measures which ensures investors are secure and returns are maximised over the elife of the investments....[+]</p></div>
<div class="btn" style="left:514px;top:1764px;width:172px;height:38px">CALL US TODAY →</div>

<!-- projects -->
<div class="abs center two" style="top:1936px"><span class="b">UPCOMING</span> <span class="g">PROJECTS</span></div>
<div class="abs proj-img" style="left:141px;background:linear-gradient(180deg,#6d8fc0,#c4d3e6 55%,#eef2f7)" role="img" aria-label="Photo of an empty warehouse interior"></div>
<div class="abs proj-img" style="left:455px;background:linear-gradient(180deg,#1d45a8 0%,#2b59c0 22%,#c9b79a 23%,#8a7a66 100%)" role="img" aria-label="Photo of a historic stone building"></div>
<div class="abs proj-img" style="left:767px;background:linear-gradient(180deg,#d9d6d0,#9a958c 60%,#c7c2b8)" role="img" aria-label="Photo of a modern office lobby"></div>
<div class="abs proj-card" style="left:162px"><h4>Hollowmere Business Park</h4><p>The Hollowmere Business Park in Cresfield, British Columbia on Vaancouver...(+)</p></div>
<div class="abs proj-card" style="left:476px"><h4>Cresfield Business Park</h4><p>The city of Cresfield is a core municipalty in the Western Communities...(+)</p></div>
<div class="abs proj-card" style="left:788px;width:250px;padding:14px 10px"><h4 style="font-size:14.5px">Mt. Corwin Ridge Professional</h4><p>Mt. Corwin Professional building will feature a repurposed building adjacent...(+)</p></div>
<div class="abs arrow" style="left:86px;background:#fff;border:1px solid #ccc"><svg width="10" height="10" viewBox="0 0 10 10" fill="none" stroke="#333" stroke-width="1.6"><path d="M6.5 1.5L3 5l3.5 3.5"/></svg></div>
<div class="abs arrow" style="left:1080px;background:var(--green)"><svg width="10" height="10" viewBox="0 0 10 10" fill="none" stroke="#fff" stroke-width="1.6"><path d="M3.5 1.5L7 5 3.5 8.5"/></svg></div>

<!-- team -->
<div class="abs soft"></div>
<div class="abs tab" style="left:386px;width:174px;color:var(--blue)">OUR PARTNERS</div>
<div class="abs tab" style="left:578px;width:235px;background:var(--green);border-color:var(--green);color:#fff">OUR MANAGEMENT TEAM</div>
<div class="abs team" style="left:141px">
  <div class="ph" style="background:linear-gradient(180deg,#6a6a6a,#bdbdbd)" role="img" aria-label="Portrait photo of Gil Parkes"></div>
  <div class="info"><h5>Gil Parkes</h5><div class="co">soundpoise</div><p>Lorem ipsum dolor sit amet, uirhtgiij consectetuer adipiscing elit, sedgtdl diam nonummy nibh euismod afweq tincidunt ut laoreet dolore magnafrt aliquam erat volutpat.</p></div>
</div>
<div class="abs team" style="left:621px">
  <div class="ph" style="background:linear-gradient(180deg,#7fb4d9,#3f6f8c)" role="img" aria-label="Portrait photo of Milos Vendraker"></div>
  <div class="info"><h5>Milos Vendraker</h5><div class="co" style="font-size:17px">QRT Dental</div><p>Lorem ipsum dolor sit amet, uirhtgiij consectetuer adipiscing elit, sedgtdl diam nonummy nibh euismod afweq tincidunt ut laoreet dolore magnafrt aliquam erat volutpat.</p></div>
</div>

<!-- newsletter -->
<div class="abs news-art" role="img" aria-label="Illustration of an open envelope holding a letter"></div>
<div class="abs news-h two"><span class="b">NEWSLETTER</span> <span class="g">SIGN UP</span></div>
<div class="abs news-q">Would you like to be kept up to date on all news and information?</div>
<div class="abs news-s">Enter your email address below to add it to our mailing list.</div>
<div class="abs field">E-Mail-Addresse</div>
<div class="btn" style="left:849px;top:3191px;width:141px;height:50px;font-size:14.5px">SUBSCRIBE →</div>

<!-- footer -->
<div class="abs foot"></div>
<div class="abs fnav" style="left:329px">HOME</div>
<div class="abs sep" style="left:411px"></div>
<div class="abs fnav" style="left:453px">ABOUT US</div>
<div class="abs sep" style="left:564px"></div>
<div class="abs fnav" style="left:606px">WHAT WE DO</div>
<div class="abs sep" style="left:739px"></div>
<div class="abs fnav" style="left:781px">CONTACT US</div>
<div class="abs fline" style="top:3422px"></div>
<div class="abs fi" style="left:142px"><span class="c"><svg width="14" height="14" viewBox="0 0 24 24" fill="#fff"><path d="M6.6 10.8a15 15 0 0 0 6.6 6.6l2.2-2.2a1 1 0 0 1 1-.25 11.4 11.4 0 0 0 3.6.57 1 1 0 0 1 1 1V20a1 1 0 0 1-1 1A17 17 0 0 1 3 4a1 1 0 0 1 1-1h3.5a1 1 0 0 1 1 1c0 1.25.2 2.450.57 3.57a1 1 0 0 1-.25 1z"/></svg></span><div><b>Call Us</b><small>+1 555 014 2288</small></div></div>
<div class="abs vsep" style="left:364px"></div>
<div class="abs fi" style="left:453px"><span class="c"><svg width="14" height="11" viewBox="0 0 24 18" fill="#fff"><path d="M0 0h24v2l-12 8L0 2z"/><path d="M0 5l12 8 12-8v13H0z"/></svg></span><div><b>Email</b><small>info@velnoragroup.ca</small></div></div>
<div class="abs vsep" style="left:737px"></div>
<div class="abs fi" style="left:826px"><span class="c"><svg width="12" height="15" viewBox="0 0 12 16" fill="#fff"><path d="M6 0a6 6 0 0 0-6 6c0 4.5 6 10 6 10s6-5.5 6-10a6 6 0 0 0-6-6zm0 8.3A2.3 2.3 0 1 1 6 3.7a2.3 2.3 0 0 1 0 4.6z"/></svg></span><div><b>Address</b><small>123, Lorem Ipsum dolor sit ame<br>Lorem Ipsum is simply dumm</small></div></div>
<div class="abs fline" style="top:3538px"></div>
<div class="abs copy">Copyright © 2020 VEL-NORA GROUP. All Rights Reserved.</div>
<div class="abs soc" style="left:969px"></div>
<div class="abs soc" style="left:1002px"></div>
<div class="abs soc" style="left:1035px"></div>

</body>
</html>
```